Maplers Report Design for Senior Care REIT

We have pulled high-level summary information from a Mapler Report, and compiled what we care about into the attached document. We would like you to take the information in the document and create a visual sheet, flyer, or slide deck (option to best layout based on info and creative vision). This should be QVN branded (logo attached) and should reflect design elements and vibes that you see on (qvnreit.example). This visual is for our executive team and should be extremely easy to read with engaging visuals for the stats included. Please include a cover page.

Target Market(s)

Corporate Executive Team

Industry/Entity Type

Senior Housing

Other font styles liked:
• Canada Type Gibson

Colors
0054AA
0677BA
7BADD7
CADEEF
E8F1F8

Requirements
Must have
• QVN branding, include all information on provided doc

```html
<!DOCTYPE html>
<html lang="en">
<head>
<meta charset="utf-8">
<title>QVN REIT – Respondents</title>
<link href="https://fonts.googleapis.com/css2?family=Figtree:wght@400;500;600;700;800&display=swap" rel="stylesheet">
<style>
:root{
  --backdrop:#595a66;
  --sky:#8cc8e6;
  --sky-deep:#76b6d9;
  --navy:#0a3a9c;
  --ink:#1d1d24;
  --card:#8ccbe8;
  --head:#8ccbe8;
  --white:#ffffff;
}
*{margin:0;padding:0;box-sizing:border-box}
html,body{width:1200px;height:2763px;overflow:hidden;background:var(--backdrop)}
body{font-family:"Figtree",Arial,sans-serif;color:var(--ink);position:relative}
.sheet{position:absolute;left:87px;top:99px;width:1026px;height:2564px;background:linear-gradient(180deg,var(--sky-deep),var(--sky))}
.inner{position:absolute;left:112px;top:123px;width:977px;height:2515px;background:var(--white);border:2px solid var(--navy)}
.photo{position:absolute;left:87px;top:99px;width:1026px;height:716px;background:linear-gradient(160deg,#e9e6e3 0%,#d4ccc4 45%,#b7aa9a 75%,#c9bcae 100%)}
.photo-frame{position:absolute;left:112px;top:123px;width:977px;height:692px;border:2px solid var(--navy);border-bottom:none}
.brand{position:absolute;left:150px;top:190px;display:flex;align-items:center;gap:14px}
.brand-square{width:44px;height:44px;background:var(--navy)}
.brand-name{font-weight:800;font-size:46px;color:var(--navy);letter-spacing:1px}
.title-box{position:absolute;left:145px;top:781px;width:910px;height:189px;background:var(--navy);color:var(--white);text-align:center}
.title-box h1{font-weight:600;font-size:96px;line-height:1;margin-top:14px;letter-spacing:1px}
.title-box p{font-size:23px;line-height:26px;margin-top:26px}
.group{position:absolute;top:987px;height:236px;background:var(--card);padding:54px 14px 0 12px}
.group h2{position:absolute;left:0;top:13px;height:30px;background:var(--navy);color:var(--white);font-size:24px;font-weight:600;line-height:30px;padding-left:12px;clip-path:polygon(0 0,88% 0,100% 100%,0 100%)}
.group p{font-size:20px;line-height:21.5px}
.summary{position:absolute;left:167px;top:1240px;width:866px;font-size:19.5px;line-height:26px;text-align:justify}
.summary b{color:var(--navy);font-weight:600}
.banner{position:absolute;left:143px;top:1373px;width:913px;height:56px;background:var(--navy);color:var(--white);font-size:31px;line-height:56px;text-align:center}
.location{position:absolute;left:167px;top:1443px;width:866px;font-size:19.5px;line-height:24px}
.col{position:absolute;top:1524px;height:846px;background:var(--navy)}
.col-head{position:absolute;background:var(--head);color:var(--navy);text-align:center}
.col-head .big{font-size:31px;font-weight:600}
.col-head .sm{font-size:20px}
.col-head .caps{font-size:21px;font-weight:600}
.sub-head{position:absolute;top:1666px;height:82px;background:var(--head);color:var(--navy);font-size:16px;line-height:17px;padding:6px 8px 0 8px}
.list{position:absolute;list-style:none;color:var(--white);font-size:16.5px;line-height:18px}
.list li{position:relative;padding-left:20px}
.list li::before{content:"";position:absolute;left:2px;top:4px;width:9px;height:9px;background:var(--sky);transform:rotate(45deg)}
.list b{font-weight:700}
.facts{position:absolute;left:150px;top:2405px;width:910px}
.fact{position:relative;height:72px;padding-left:59px;font-size:19.5px;line-height:25px;font-weight:600}
.fact span{font-weight:400}
.fact svg{position:absolute;left:3px;top:6px}
</style>
</head>
<body>
<div class="sheet"></div>
<div class="inner"></div>
<div class="photo" role="img" aria-label="Photo of three women reviewing a printed chart together at a table"></div>
<div class="photo-frame"></div>
<div class="brand"><div class="brand-square"></div><div class="brand-name">QVN</div></div>

<section class="title-box">
  <h1>RESPONDENTS</h1>
  <p>were categorized in one of three groups based on their likelihood of moving<br>to an age-qualified community in the future:</p>
</section>

<section class="group" style="left:151px;width:288px">
  <h2 style="width:240px">PROBABLES</h2>
  <p>Respondents who were likely or very likely to move to a residential community with services where the permanent residents must be a minimum of 55 years of age.</p>
</section>
<section class="group" style="left:457px;width:286px">
  <h2 style="width:240px">POSSIBLES</h2>
  <p>Respondents who were unsure if they would move to a residential community where the permanent residents must be a minimum of 55 years of age.</p>
</section>
<section class="group" style="left:769px;width:287px">
  <h2 style="width:240px">IMPROBABLES</h2>
  <p>Respondents who were unlikely or very unlikely to move to a residential community where the permanent residents must be a minimum of 55 years of age.</p>
</section>

<p class="summary">The top five in-unit amenities ranked by all respondents were full <b>KITCHEN</b> (refrigerator, stove/oven, microwave); <b>LAUNDRY</b> room with washer/dryer; <b>LIVING ROOM</b> or great room; lots of <b>WINDOWS</b> for plenty of natural light; and additional <b>STORAGE SPACE</b> for seasonal or occasionally used items.</p>

<div class="banner">Most preferred location among Probables and Possibles:</div>
<p class="location">Outlying suburban (outer edge developed areas of a city where there are more single-family homes and neighborhoods and fewer commercial areas) <b>(43%)</b></p>

<div class="col" style="left:151px;width:296px"></div>
<div class="col" style="left:457px;width:294px"></div>
<div class="col" style="left:760px;width:296px"></div>

<div class="col-head" style="left:162px;top:1535px;width:275px;height:213px;padding-top:20px;line-height:25px">
  <div class="big">59% <span class="sm">of</span></div>
  <div class="caps">PROBABLES<br>&amp;<br>POSSIBLES</div>
  <div class="sm" style="line-height:26px">rated the following<br>as essential or desirable:</div>
</div>
<div class="col-head" style="left:468px;top:1535px;width:577px;height:131px;padding-top:6px;line-height:25px">
  <div class="big">55% <span class="sm">and</span> 61% <span class="sm">of</span></div>
  <div class="caps">PROBABLES AND POSSIBLES,</div>
  <div class="sm">respectively, would prefer to<br>receive care “In my residence”</div>
</div>
<div class="sub-head" style="left:468px;width:273px">“Desirable + essential” preferences for common area amenities among Probables &amp; Possibles: 45%</div>
<div class="sub-head" style="left:770px;width:275px">“Desirable + essential” preferences for common area amenities among Probables &amp; Possibles broken up by age group (55-74 – 75+):</div>

<ul class="list" style="left:158px;top:1764px;width:285px">
  <li style="margin-bottom:17px">Full kitchen with refrigerator, stove/oven and microwave</li>
  <li style="margin-bottom:17px">Laundry room with washer/dryer</li>
  <li style="margin-bottom:17px">Living room or great room</li>
  <li style="margin-bottom:17px">Lots of windows for plenty of natural light</li>
  <li style="margin-bottom:17px">Additional storage space for seasonal or occasionally used items</li>
  <li style="margin-bottom:17px">Fiber-Optic Internet/Gigabit Internet</li>
  <li style="margin-bottom:17px">Walk-in closet</li>
  <li style="margin-bottom:14px">Open porch, patio, or balcony</li>
  <li style="margin-bottom:14px">Dining area in the kitchen</li>
  <li style="margin-bottom:14px">Screened porch, patio, or balcony</li>
  <li style="margin-bottom:14px">Study or den</li>
  <li>Enclosed porch, patio, or balcony</li>
</ul>

<ul class="list" style="left:462px;top:1764px;width:285px">
  <li style="margin-bottom:17px">Walking trails <b>64%</b></li>
  <li style="margin-bottom:17px">On-site storage units <b>55%</b></li>
  <li style="margin-bottom:17px">Indoor fitness center <b>54%</b></li>
  <li style="margin-bottom:17px">Activity room <b>52%</b></li>
  <li style="margin-bottom:17px">Convenience store <b>52%</b></li>
  <li style="margin-bottom:17px">A family-friendly lounge <b>52%</b></li>
  <li style="margin-bottom:17px">ATM <b>50%</b></li>
  <li style="margin-bottom:17px">Multi-purpose room: group meetings, classes, card room, etc. <b>49%</b></li>
  <li style="margin-bottom:17px">Library <b>47%</b></li>
  <li style="margin-bottom:17px">Indoor swimming pool <b>46%</b></li>
  <li style="margin-bottom:17px">Beauty salon/barbershop <b>45%</b></li>
  <li style="margin-bottom:17px">Visiting doctor's clinic <b>42%</b></li>
  <li style="margin-bottom:17px">Indoor running/walking track <b>41%</b></li>
  <li style="margin-bottom:17px">Media room/movie room <b>41%</b></li>
  <li>Outdoor grilling stations <b>40%</b></li>
</ul>

<ul class="list" style="left:763px;top:1764px;width:292px">
  <li style="margin-bottom:17px">Walking trails <b>67% – 59%</b></li>
  <li style="margin-bottom:17px">Indoor fitness center <b>55% – 52%</b></li>
  <li style="margin-bottom:17px">On-site storage units <b>54% – 56%</b></li>
  <li style="margin-bottom:17px">Activity room <b>52% – 52%</b></li>
  <li style="margin-bottom:17px">ATM <b>51% – 48%</b></li>
  <li style="margin-bottom:17px">Convenience store <b>51% – 52%</b></li>
  <li style="margin-bottom:17px">A family-friendly lounge <b>49% – 56%</b></li>
  <li style="margin-bottom:17px">Indoor swimming pool <b>48% – 42%</b></li>
  <li style="margin-bottom:17px">Multi-purpose room: group meetings, classes, card room, etc. <b>47% – 51%</b></li>
  <li style="margin-bottom:17px">Outdoor grilling stations <b>45% – 34%</b></li>
  <li style="margin-bottom:17px">Library <b>44% – 51%</b></li>
  <li style="margin-bottom:17px">Outdoor swimming pool <b>44% – 30%</b></li>
  <li style="margin-bottom:17px">Beauty salon/barbershop <b>43% – 49%</b></li>
  <li style="margin-bottom:17px">Indoor running/walking track <b>43% – 38%</b></li>
  <li>Visiting doctor's clinic <b>42% – 42%</b></li>
</ul>

<div class="facts">
  <div class="fact">
    <svg width="42" height="42" viewBox="0 0 42 42"><circle cx="21" cy="21" r="18" fill="none" stroke="#0a3a9c" stroke-width="4"/><path d="M12 21 l7 7 l12 -13" fill="none" stroke="#0a3a9c" stroke-width="4" stroke-linecap="round" stroke-linejoin="round"/></svg>
    29% of Possibles &amp; Probables considered it essential and 35% considered themselves indifferent to having a pet-friendly community
  </div>
  <div class="fact">
    <svg width="42" height="42" viewBox="0 0 42 42"><circle cx="21" cy="21" r="18" fill="none" stroke="#0a3a9c" stroke-width="4"/><path d="M12 21 l7 7 l12 -13" fill="none" stroke="#0a3a9c" stroke-width="4" stroke-linecap="round" stroke-linejoin="round"/></svg>
    69% of Possibles &amp; Probables prefer Dining Out as a desired activity <span>(community proximity to restaurants is a must)</span>
  </div>
  <div class="fact">
    <svg width="42" height="42" viewBox="0 0 42 42"><circle cx="21" cy="21" r="18" fill="none" stroke="#0a3a9c" stroke-width="4"/><path d="M12 21 l7 7 l12 -13" fill="none" stroke="#0a3a9c" stroke-width="4" stroke-linecap="round" stroke-linejoin="round"/></svg>
    58% of Possibles &amp; Probables desire local travel as a possible activity <span>(47% desire travel US &amp; abroad)</span>
  </div>
</div>
</body>
</html>
```